Portrait of a Graduate

Our school community has created a document which describes the characteristics that every student who graduates from our school should possess. We would like a visual graphic to present the information to parents\ community. We came up with three buckets (Personal, Social, and Academic) and the concept "BLH Graduates Will Be Okay" is the central theme.
We are open to 2 different concepts:
1. A ven diagram of sorts, where the three buckets are each in an area - and the over lap is "BLH Graduates Will Be Okay"
2. Our logo has a sassafras leaf in it - using the leaves to represent each bucket and the central concept as the stem - or some other creative version.

The text to be used is below:

BLH Graduates Will Be Okay (at the center/on the stem)

1. Personal
They will:
have self-worth
advocate for themselves
feel secure in their future

2. Social
They will:
embrace differences
engage in trusting relationships
be compassionate (members of their community)

3. Academic
They will:
apply skills and strategies
creatively problem-solve
achieve individual success

```html
<!DOCTYPE html>
<html lang="en">
<head>
<meta charset="utf-8">
<title>Portrait of a Graduate — BLH Graduates Will Be Okay</title>
<link rel="stylesheet" href="https://fonts.googleapis.com/css2?family=Marcellus&family=Cardo&display=swap">
<style>
  :root {
    --navy: #02344a;
    --gold: #e3bd22;
    --green: #024b2b;
    --core: #e9e9e9;
    --ink: #111111;
    --white: #ffffff;
    --icon-navy-tone: #2b5368;
    --icon-gold-tone: #0f3a4a;
    --icon-green-tone: #2a6a4a;
  }
  html, body {
    margin: 0;
    padding: 0;
    width: 1200px;
    height: 1200px;
    overflow: hidden;
    background: var(--white);
  }
  .graduate-portrait {
    display: block;
    width: 1200px;
    height: 1200px;
  }
  .heading { font-family: "Marcellus", serif; }
  .body-copy { font-family: "Cardo", serif; font-size: 25px; }
  .numeral { font-family: "Marcellus", serif; font-size: 150px; }
  .on-dark { fill: var(--white); }
  .on-gold { fill: var(--navy); }
  .core-title { font-family: "Marcellus", serif; fill: var(--ink); }
  .school-name { font-family: "Marcellus", serif; fill: var(--navy); font-size: 40px; }
</style>
</head>
<body>
<svg class="graduate-portrait" viewBox="0 0 1200 1200" xmlns="http://www.w3.org/2000/svg">
  <defs>
    <mask id="outside-personal">
      <rect width="1200" height="1200" fill="#fff"/>
      <circle cx="419" cy="446" r="364" fill="#000"/>
    </mask>
  </defs>

  <!-- circles -->
  <circle class="ring-social" cx="784" cy="527" r="363" fill="var(--gold)"/>
  <circle class="ring-personal" cx="419" cy="446" r="364" fill="var(--navy)"/>
  <circle class="ring-academic" cx="481" cy="744" r="352" fill="var(--green)"/>
  <circle class="ring-social-front" cx="784" cy="527" r="363" fill="var(--gold)" mask="url(#outside-personal)"/>
  <circle class="core" cx="583" cy="557" r="164" fill="var(--core)"/>

  <!-- personal -->
  <text class="heading on-dark" x="240" y="216" font-size="56">PERSONAL</text>
  <g class="body-copy on-dark" text-anchor="end">
    <text x="503" y="259">They will:</text>
    <text x="503" y="289">have self-worth</text>
    <text x="503" y="319">advocate for themselves</text>
    <text x="503" y="349">feel secure in their future</text>
  </g>
  <g class="bullets" fill="var(--white)">
    <circle cx="530" cy="282" r="7"/>
    <circle cx="530" cy="312" r="7"/>
    <circle cx="530" cy="342" r="7"/>
  </g>
  <text class="numeral on-dark" x="555" y="337">01</text>
  <rect class="icon-person" x="104" y="294" width="112" height="161" rx="40" fill="var(--icon-navy-tone)" role="img" aria-label="Person icon"/>

  <!-- social -->
  <rect class="icon-network" x="800" y="236" width="197" height="192" rx="20" fill="var(--icon-gold-tone)" opacity="0.35" role="img" aria-label="Icon of connected people"/>
  <text class="heading on-gold" x="810" y="494" font-size="80">SOCIAL</text>
  <g class="body-copy on-gold">
    <text x="811" y="541">They will:</text>
    <text x="811" y="571">embrace differences</text>
    <text x="811" y="601">engage in trusting relationships</text>
    <text x="811" y="631">be compassionate (members of</text>
    <text x="811" y="661">their community)</text>
  </g>
  <g class="bullets" fill="var(--navy)">
    <circle cx="791" cy="564" r="7"/>
    <circle cx="791" cy="594" r="7"/>
    <circle cx="791" cy="624" r="7"/>
  </g>
  <text class="numeral on-gold" x="606" y="828">02</text>

  <!-- academic -->
  <text class="numeral on-dark" x="240" y="614">03</text>
  <text class="heading on-dark" x="171" y="720" font-size="56">ACADEMIC</text>
  <g class="body-copy on-dark">
    <text x="207" y="786">They will:</text>
    <text x="207" y="822">apply skills and strategies</text>
    <text x="207" y="857">creatively problem-solve</text>
    <text x="207" y="894">achieve individual success</text>
  </g>
  <g class="bullets" fill="var(--white)">
    <circle cx="183" cy="815" r="7"/>
    <circle cx="183" cy="851" r="7"/>
    <circle cx="183" cy="887" r="7"/>
  </g>
  <rect class="icon-cap" x="420" y="930" width="201" height="139" rx="16" fill="var(--icon-green-tone)" role="img" aria-label="Graduation cap icon"/>

  <!-- centre theme -->
  <g class="core-title" text-anchor="middle">
    <text x="583" y="588" font-size="36">BLH GRADUATES</text>
    <text x="583" y="630" font-size="42">WILL BE OKAY</text>
  </g>

  <!-- school name -->
  <g class="school-name" text-anchor="end">
    <text x="1166" y="1110">BRAMBLE LANE</text>
    <text x="1166" y="1160">HOUSE</text>
  </g>
</svg>
</body>
</html>
```